依頼詳細
・デザイン概要
今回は、トップページデザインの募集になります。
レスポンシブデザインのサイトで、bootstrap4を利用しコーディングする予定になります。
デザイン幅は2000px、コンテンツの幅はbootstrap4デフォルトの1110pxを基準としてください。ただし最近のデザインの流行を取りいれて、フルワイドや、1200~15000px程度の幅のコンテンツをバランスよくレイアウトしてください。
コンテンツ配置は基本12分割になります。がデザインによっては、多少逸脱してもかまいません。
(12分割のコンテンツ幅については添付のPSDを参考にご覧ください)

本文のフォントはゴシック系は游ゴシック、メイリオ、明朝系は遊明朝でお願いします。
飾り文字はフリーフォントか、googleフォントを利用してください。

メイン画像部分・グローバルメニューは、ワイド適用でお願いします。

掲載画像については、基本は添付ファイルを使用してください。
また、雰囲気が合っていれば、指定外の画像を追加掲載いただいてOKです。

・その他
デザイン・ムード、参考サイトについてなど、掲載内容詳細に関しては、別添のExcel資料を参照してください。

資料上はサイト名(社名)や住所などは伏字にしております。ご提案時点ではそのまま作成をお願いします。当選確定後、本内容に修正をお願いいたします。

当選の方は、希望があれば引き続き下層ページの作成及びコーディング作業を依頼可能です。
ページ数
1ページ
希望イメージ
シンプル 複雑
単色 カラフル
暗い 明るい
日常 高級
遊び心 厳粛
未来的 伝統的
女性的 男性的
希望する色
青系
納品ファイル
• 高解像度JPG (.jpg)
• フォトショップ形式 (.psd)

クライアントと折衝しまして、norvikaplane様のデザインが一番「落ち着いてる雰囲気」と「町工場な印象」を感じたとのことで、当選とさせていただきました。

本件、多数のご提案ありがとうございました。
どの提案もとてもよく、クライアントもかなり悩んでいましたがら、最終的にムードや印象の部分でnorvikaplane様を当選とさせていいただきました。
どうもありがとうございました。
今後とも宜しくお願いいたします。

```html
<!DOCTYPE html>
<html lang="ja">
<head>
<meta charset="utf-8">
<title>Seiran Spring Works</title>
<link rel="stylesheet" href="https://fonts.googleapis.com/css2?family=Noto+Sans+JP:wght@400;500;700&family=Montserrat:ital,wght@0,600;0,700;1,800&display=swap">
<style>
:root{
  --navy:#0d2a5e;
  --deep:#081a3e;
  --blue:#1f5bb8;
  --accent:#2b6fd6;
  --sky:#8fb4e6;
  --paper:#ffffff;
  --ink:#1d2a40;
  --mute:#5b6780;
  --red:#d23b3b;
}
*{margin:0;padding:0;box-sizing:border-box}
html,body{width:828px;height:1200px;overflow:hidden;background:var(--paper)}
body{position:relative;font-family:"Noto Sans JP",sans-serif;color:var(--ink)}
.abs{position:absolute}

/* header + hero */
.hero{left:0;top:0;width:828px;height:360px;background:linear-gradient(160deg,#2d5f9f 0%,#16396f 45%,#0a2352 100%)}
.hero-clip{left:0;top:300px;width:828px;height:200px}
.brand{left:22px;top:14px;color:#fff;font-size:15px;font-weight:700;display:flex;align-items:center;gap:7px}
.brand::before{content:"";width:12px;height:12px;background:#fff;display:block}
.brand small{display:block;font-size:8px;font-weight:400;opacity:.8}
.contact-top{right:18px;top:8px;display:flex;gap:6px;flex-direction:column;align-items:flex-end}
.contact-top .note{color:#fff;font-size:8px}
.contact-top .tels{display:flex;gap:6px}
.tel{background:#fff;color:var(--red);font-family:Montserrat,sans-serif;font-weight:700;font-size:13px;padding:3px 8px;display:flex;align-items:center;gap:4px}
.tel svg{width:11px;height:11px}
.nav{left:430px;top:52px;display:flex;gap:26px;color:#fff;font-size:10px;font-weight:500}
.nav span{border-bottom:1px solid rgba(255,255,255,.6);padding-bottom:3px}
.hero-title{left:0;top:188px;width:828px;text-align:center;color:#fff;font-family:Montserrat,sans-serif;font-style:italic;font-weight:800;font-size:50px;letter-spacing:1px}

.intro-text{left:430px;top:372px;width:360px;font-size:10px;line-height:1.9;color:var(--ink)}

/* tech */
.section-head{font-size:19px;font-weight:700;color:var(--navy)}
.section-sub{font-size:10px;color:var(--mute);margin-top:2px}
.tech-head{left:52px;top:505px}
.tech-text{left:52px;top:565px;width:240px;font-size:9px;line-height:1.9;color:var(--mute)}
.more{font-family:Montserrat,sans-serif;font-size:9px;font-weight:700;color:var(--accent);display:flex;align-items:center;gap:6px}
.more::after{content:"";width:38px;height:2px;background:var(--accent)}
.tech-more{left:52px;top:706px}
.tech-photo{left:430px;top:490px;width:398px;height:230px;background:linear-gradient(135deg,#9aa7b8 0%,#5c6a80 55%,#33415a 100%)}
.tech-label{left:560px;top:670px;color:#fff;font-family:Montserrat,sans-serif;font-weight:700;font-size:30px}

/* products */
.prod-photo{left:0;top:720px;width:440px;height:235px;background:linear-gradient(135deg,#cfd6de 0%,#8d97a5 50%,#4e5a6b 100%)}
.prod-label{left:26px;top:895px;color:#fff;font-family:Montserrat,sans-serif;font-weight:700;font-size:30px}
.prod-band{left:440px;top:726px;width:388px;height:56px;background:var(--accent)}
.prod-head{left:470px;top:734px;color:#fff}
.prod-head .section-head{color:#fff}
.prod-head .section-sub{color:#dbe7fa}
.prod-text{left:470px;top:800px;width:290px;font-size:9px;line-height:1.9;color:var(--mute)}
.prod-more{left:470px;top:905px}

/* company */
.company{left:0;top:940px;width:828px;height:260px;background:linear-gradient(120deg,#163f86 0%,#0d2a5e 55%,#081a3e 100%)}
.company-en{left:200px;top:950px;color:rgba(255,255,255,.9);font-family:Montserrat,sans-serif;font-weight:700;font-size:26px;font-style:italic}
.company-head{left:40px;top:1000px;color:#fff}
.company-head .section-head{color:#fff}
.company-text{left:40px;top:1040px;width:260px;color:#cfdcf3;font-size:9px;line-height:1.9}
.company-more{left:40px;top:1082px}
.company-more.more{color:#fff}
.company-more.more::after{background:#fff}
.map{left:420px;top:960px;width:370px;height:150px;background:linear-gradient(135deg,#f1ece2,#e2e6ea)}
.footer-brand{left:100px;top:1130px;color:#fff;font-size:14px;font-weight:700}
.footer-brand small{display:block;font-size:8px;font-weight:400;color:#bcd0ef;margin-top:3px}
.footer-contact{left:420px;top:1118px;width:370px;text-align:center;color:#fff;font-size:8px}
.footer-contact .tels{display:flex;gap:8px;justify-content:center;margin-top:4px}
.footer-nav{left:420px;top:1176px;width:370px;text-align:center;color:#bcd0ef;font-size:7px}
</style>
</head>
<body>

<div class="abs hero" role="img" aria-label="青く色調補正された工場内の機械設備の写真"></div>
<svg class="abs hero-clip" width="828" height="200" viewBox="0 0 828 200">
  <polygon points="0,60 828,0 828,200 0,200" fill="#ffffff"/>
  <polygon points="0,60 330,36 300,160 0,190" fill="#0d2a5e" opacity=".9"/>
</svg>

<div class="abs brand"><div>有限会社〇〇〇〇製作所<small>Seiran Spring Works</small></div></div>
<div class="abs contact-top">
  <div class="note">お問い合わせ・ご相談はこちら（平日 9:00〜18:00）</div>
  <div class="tels">
    <div class="tel"><svg viewBox="0 0 24 24"><path fill="currentColor" d="M6.6 10.8a15 15 0 0 0 6.6 6.6l2.2-2.2c.3-.3.7-.4 1-.2 1.1.4 2.3.6 3.6.6.6 0 1 .4 1 1V20c0 .6-.4 1-1 1A17 17 0 0 1 3 4c0-.6.4-1 1-1h3.5c.6 0 1 .4 1 1 0 1.3.2 2.5.6 3.6.1.3 0 .7-.2 1z"/></svg>012-345-6789</div>
    <div class="tel"><svg viewBox="0 0 24 24"><rect x="3" y="6" width="18" height="12" fill="none" stroke="currentColor" stroke-width="2"/><path d="M3 6l9 7 9-7" fill="none" stroke="currentColor" stroke-width="2"/></svg>012-345-6798</div>
  </div>
</div>
<nav class="abs nav"><span>技術紹介</span><span>製品紹介</span><span>会社案内</span><span>お問い合わせ</span></nav>
<h1 class="abs hero-title">Seiran Spring Works</h1>

<p class="abs intro-text">〇〇〇〇製作所は、創業以来ばね製造一筋に歩んできた町工場です。圧縮ばね、引張ばね、ねじりばねから線細工品まで、一本一本を熟練の職人が丁寧に仕上げています。小ロット・試作品のご相談もお気軽にお寄せください。確かな技術と誠実な対応で、お客様のものづくりを支えてまいります。</p>

<div class="abs tech-head"><div class="section-head">技術紹介</div><div class="section-sub">熟練の技術と高い精度</div></div>
<p class="abs tech-text">長年培ってきた加工技術と最新設備により、高精度なばねを安定してお届けします。多品種少量生産にも柔軟に対応いたします。</p>
<div class="abs more tech-more">more</div>
<div class="abs tech-photo" role="img" aria-label="精密なばね部品のクローズアップ写真"></div>
<div class="abs tech-label">Technology</div>

<div class="abs prod-photo" role="img" aria-label="銀色のボルトやばね製品が並ぶ写真"></div>
<div class="abs prod-label">Products</div>
<div class="abs prod-band"></div>
<div class="abs prod-head"><div class="section-head">製品紹介</div><div class="section-sub">高精度・高品質な製品加工</div></div>
<p class="abs prod-text">圧縮・引張・ねじりばねをはじめ、各種線細工品を製造しています。用途に合わせた材質選定からご提案いたします。</p>
<div class="abs more prod-more">more</div>

<div class="abs company" role="img" aria-label="青い照明に照らされたばね素材の写真"></div>
<div class="abs company-en">Company</div>
<div class="abs company-head"><div class="section-head">会社案内</div></div>
<p class="abs company-text">会社概要・沿革・アクセス情報をご紹介します。工場見学も随時受け付けております。</p>
<div class="abs more company-more">more</div>
<div class="abs map" role="img" aria-label="会社周辺の地図"></div>
<div class="abs footer-brand">有限会社〇〇〇〇製作所<small>〒000-0000 〇〇県〇〇市〇〇町0-0-0</small><small>TEL 012-345-6789 / FAX 012-345-6798</small></div>
<div class="abs footer-contact">お問い合わせ・ご相談はお気軽に（平日 9:00〜18:00）
  <div class="tels">
    <div class="tel">012-345-6789</div>
    <div class="tel">012-345-6798</div>
  </div>
</div>
<div class="abs footer-nav">ホーム ｜ 技術紹介 ｜ 製品紹介 ｜ 会社案内 ｜ お問い合わせ</div>

</body>
</html>
```